Healthcare Fraud Criminal Defense Attorney Website

We need to design a website that effectively promotes the message that our firm is at the cutting edge of healthcare law. We want to appear to be trusted experts in the field, who are innovators. We do not want to bore our potential clients with too much content, only enough to make it look like we know what we're doing. They'll have to gain a sense of trust in us to help them once they come to the website. At some part there will have to be room for 3 pictures of the 3 lawyers and a description of who they are.
Updates

Also this is a website that we think looks good: http://www.marvelinlegal.example/

Target Market(s)

Nurses, Doctors and owners of healthcare businesses that have been arrested and/or charged with fraud. They also may have simply been notified that they are under investigation.

Industry/Entity Type

Legal

Number of Pages Required

3 page

Font styles to use
Serif

Colors
000000
606060
b2b2b2
f5f5f5

Requirements
Must have
• A homepage with some content relative to the field. It will likely have 3 or 4 paragraphs with distinct content in each.
• Another page in the website that has a good layout for introducing the 3 attorneys involved.
• Possibly a professional looking "frequently asked questions" third page.
Nice to have
• A call-to-action or info-submission area that does not look cheesy or follow you around the page but is still readily available.
• A phone number must be prominently displayed.

```html
<!DOCTYPE html>
<html lang="en">
<head>
<meta charset="utf-8">
<title>Marvelin Legal — Healthcare Fraud Defense</title>
<link href="https://fonts.googleapis.com/css2?family=Tinos:wght@400;700&family=Open+Sans:wght@400;600;700&display=swap" rel="stylesheet">
<style>
:root{
  --black:#000000;
  --ink:#111111;
  --grey:#606060;
  --silver:#b2b2b2;
  --light:#f5f5f5;
  --white:#ffffff;
  --line:#dddddd;
  --serif:"Tinos",serif;
  --sans:"Open Sans",sans-serif;
}
*{box-sizing:border-box;margin:0;padding:0}
html,body{width:1200px;height:3930px;overflow:hidden;background:var(--white);font-family:var(--serif);color:var(--ink)}
.page{position:relative;width:1200px;height:3930px}
.wrap{position:absolute;left:59px;width:1102px}

/* top bar */
.topbar{top:0;height:40px;display:flex;align-items:center;justify-content:flex-end;font-family:var(--sans);font-size:10px;font-weight:700;text-transform:uppercase}
.topbar .info{position:absolute;left:190px}
.topbar .social{display:flex;gap:22px;margin-right:30px}
.topbar .social span{width:9px;height:9px;border-radius:50%;background:var(--ink)}
.topbar .login{display:flex;align-items:center;gap:6px}
.nav{top:40px;height:45px;display:flex;justify-content:center;border-top:1px solid var(--line)}
.nav a{font-family:var(--sans);font-size:10.5px;font-weight:700;color:var(--ink);text-decoration:none;padding:14px 17px}

/* hero */
.hero{top:85px;height:490px;background:linear-gradient(90deg,#0c0c0c,#2a2a2a 50%,#141414);overflow:hidden}
.hero .portrait{position:absolute;left:250px;top:0;width:430px;height:490px;background:radial-gradient(ellipse at 50% 40%,#6a5b52 0%,#3a3330 40%,#1a1a1a 75%)}
.hero .text{position:absolute;left:566px;top:95px;width:500px;color:var(--white)}
.hero h1{font-weight:400;font-size:48px;letter-spacing:3px;line-height:1}
.hero .tag{display:inline-block;margin-top:14px;background:var(--black);border:1px solid #333;padding:6px 16px;font-size:20px;letter-spacing:3px}
.hero p{margin-top:22px;font-size:13.5px;line-height:1.45;color:#cfcfcf}
.btn-line{display:inline-block;margin-top:40px;border:2px solid var(--white);color:var(--white);font-family:var(--sans);font-size:12px;font-weight:600;padding:12px 34px}
.brand{position:absolute;left:59px;top:0;width:161px;height:175px;background:var(--black);color:var(--white);display:flex;flex-direction:column;align-items:center;justify-content:flex-end;padding-bottom:24px;gap:14px;z-index:2}
.brand .mark{width:48px;height:48px;border-radius:50%;background:#2ea64a}
.brand .name{font-family:var(--sans);font-weight:600;font-size:16px;text-align:center;line-height:1.1}

/* intro */
.intro{top:590px;height:405px;background:var(--light);text-align:center}
.intro h2{margin-top:45px;font-weight:400;font-size:42px;line-height:1.25}
.services{display:flex;justify-content:space-between;padding:0 100px;margin-top:40px}
.service{width:240px}
.service svg{display:block;margin:0 auto 10px}
.service h3{font-weight:400;font-size:26px}
.service p{font-size:13px;color:var(--grey);line-height:1.35;margin-top:6px}
.service a{display:block;margin-top:16px;font-size:15px;color:var(--ink);text-decoration:none}

/* cta band */
.cta{top:997px;height:118px;background:var(--black);display:flex;align-items:center;justify-content:center;gap:50px;color:#d0d0d0;font-size:15px}
.cta .btn{background:var(--silver);color:var(--ink);font-family:var(--sans);font-size:14px;letter-spacing:3px;padding:12px 28px}

/* gallery */
.gallery{top:1115px;height:225px;display:flex}
.gallery div{flex:1}
.g1{background:linear-gradient(135deg,#1d1d1d,#3b3b3b);position:relative}
.g1 .ico{position:absolute;top:88px;width:50px;height:50px;border:2px solid var(--white);border-radius:50%;display:flex;align-items:center;justify-content:center}
.g2{background:linear-gradient(135deg,#6b6e72,#3c3f44)}
.g3{background:linear-gradient(180deg,#b58b3c,#6b4a22)}
.g4{background:linear-gradient(180deg,#c9cfd6,#5a6068)}
.g5{background:linear-gradient(180deg,#8a7a66,#3d342c)}

/* attorneys */
.attorneys{top:1340px;height:620px;text-align:center}
.attorneys h2{margin-top:35px;font-weight:400;font-size:42px}
.cards{display:flex;justify-content:space-between;margin-top:38px}
.card{width:350px;border:1px solid var(--line)}
.card .photo{height:293px;background:linear-gradient(180deg,#d9d2cc,#9a8f86)}
.card .photo.dark{background:linear-gradient(180deg,#3a3a3a,#1a1a1a);display:flex;align-items:center;justify-content:center;gap:14px}
.card .photo.dark span{width:12px;height:12px;border-radius:50%;background:var(--white)}
.card h4{font-weight:400;font-size:15px;margin-top:14px;text-transform:uppercase}
.card p{font-size:12px;color:var(--grey);margin:4px 0 14px}
.dots{display:flex;justify-content:center;gap:8px;margin-top:38px}
.dots span{width:11px;height:11px;border:1px solid var(--grey);border-radius:50%}
.dots span.on{background:var(--grey)}

/* stats */
.stats{top:1980px;height:377px;display:flex;justify-content:space-between}
.stat{width:540px;color:var(--white);text-align:center;padding-top:90px}
.stat.s1{background:linear-gradient(135deg,#4a4a4a,#2b2b2b)}
.stat.s2{background:linear-gradient(135deg,#262626,#5a5a5a)}
.stat .cur{font-size:30px;height:34px}
.stat .num{font-size:36px;line-height:1.1}
.stat .lab{font-size:14px;text-transform:uppercase;margin-top:6px}
.stat p{font-size:16px;line-height:1.2;margin:6px auto 0;width:270px}

.blog{top:2405px;height:45px;display:flex;justify-content:center}
.blog span{background:var(--black);color:var(--white);font-family:var(--sans);font-size:12px;font-weight:600;padding:14px 30px}
.partners{top:2520px;height:140px;border-top:1px solid var(--line);left:150px;width:900px;display:flex;justify-content:space-around;align-items:center}
.partners span{width:84px;height:56px;background:#d8d8d8}

/* contact band */
.contact{top:2781px;height:206px;background:var(--black);color:var(--white);display:flex;justify-content:space-around;text-align:center;font-size:15px;line-height:1.4}
.contact .col{width:300px;position:relative;padding-top:75px}
.contact .icon{position:absolute;left:120px;top:-18px;width:60px;height:56px;background:var(--white);display:flex;align-items:center;justify-content:center}

/* form */
.write{top:2987px;height:600px;background:var(--light);text-align:center}
.write h2{margin-top:35px;font-weight:400;font-size:44px}
.write .sub{font-size:13px;color:var(--grey)}
.form{width:730px;margin:55px auto 0;display:grid;grid-template-columns:1fr 1fr;gap:14px 30px;text-align:left}
.field{background:var(--white);border:1px solid var(--line);height:36px;font-family:var(--sans);font-size:9.5px;color:var(--grey);padding:11px 8px;text-transform:uppercase}
.field.msg{grid-column:1/3;height:200px}
.send{display:inline-block;margin-top:40px;background:var(--black);color:var(--white);font-family:var(--sans);font-size:12px;font-weight:600;padding:14px 30px}

/* footer */
.footer{top:3592px;height:300px;background:var(--black);color:#ccc;display:flex;gap:40px;padding:40px 60px 0}
.footer .fcol{flex:1;font-size:11.5px;line-height:1.6}
.footer h5{font-family:var(--sans);font-size:13px;color:var(--white);letter-spacing:1px;margin-bottom:18px}
.tweet{display:flex;gap:10px;margin-bottom:16px}
.tweet i{flex:none;width:10px;height:10px;border-radius:50%;background:#999;margin-top:4px}
.footer .row{border-bottom:1px solid #333;padding:5px 0}
.copy{top:3892px;height:38px;display:flex;align-items:center;justify-content:center;font-size:11px;color:var(--grey)}
</style>
</head>
<body>
<div class="page">

  <div class="brand"><span class="mark"></span><span class="name">MARVELIN LEGAL</span></div>

  <div class="wrap topbar">
    <span class="info">Free Case Review: +1 555 014 2290</span>
    <span class="social"><span></span><span></span><span></span><span></span></span>
    <span class="login">
      <svg width="9" height="10" viewBox="0 0 9 10"><circle cx="4.5" cy="3" r="2.5" fill="#111"/><path d="M0 10a4.5 4 0 0 1 9 0z" fill="#111"/></svg>
      Login/Register
    </span>
  </div>
  <nav class="wrap nav"><a>HOME</a><a>ABOUT US</a><a>ATTORNEYS</a><a>FAQ</a><a>CONTACT US</a></nav>

  <header class="wrap hero">
    <div class="portrait" role="img" aria-label="Portrait photo of the lead attorney in a dark suit and red tie"></div>
    <div class="text">
      <h1>MARVELIN LEGAL</h1>
      <div class="tag">HEALTHCARE FRAUD DEFENSE</div>
      <p>Charged with healthcare fraud or told you are under investigation? Our attorneys defend nurses, doctors and clinic owners with a modern, evidence-driven approach to billing, Medicare and licensing cases.</p>
      <span class="btn-line">KNOW MORE</span>
    </div>
  </header>

  <section class="wrap intro">
    <h2>Trusted Defense for Healthcare Professionals<br>Facing Fraud Charges</h2>
    <div class="services">
      <div class="service">
        <svg width="36" height="40" viewBox="0 0 36 40"><circle cx="18" cy="11" r="9" fill="#b2b2b2"/><path d="M2 40a16 14 0 0 1 32 0z" fill="#b2b2b2"/></svg>
        <h3>Fraud Defense</h3>
        <p>Billing, kickback and Medicare fraud charges defended at trial.</p>
        <a>Know More</a>
      </div>
      <div class="service">
        <svg width="36" height="40" viewBox="0 0 36 40"><path d="M9 18v-6a9 9 0 0 1 18 0v6" fill="none" stroke="#b2b2b2" stroke-width="4"/><rect x="4" y="18" width="28" height="20" rx="2" fill="#b2b2b2"/></svg>
        <h3>Investigations</h3>
        <p>Early counsel when agents, auditors or subpoenas arrive.</p>
        <a>Know More</a>
      </div>
      <div class="service">
        <svg width="40" height="40" viewBox="0 0 40 40"><circle cx="20" cy="20" r="16" fill="none" stroke="#b2b2b2" stroke-width="4"/><path d="M20 10v11h8" fill="none" stroke="#b2b2b2" stroke-width="3.5"/></svg>
        <h3>License Defense</h3>
        <p>Protecting your licence and practice before medical boards.</p>
        <a>Know More</a>
      </div>
    </div>
  </section>

  <section class="wrap cta">
    <span>Under investigation? Call 1 (555) 014-2684 for a confidential case review today.</span>
    <span class="btn">CONTACT</span>
  </section>

  <section class="wrap gallery">
    <div class="g1" role="img" aria-label="Dark office interior photo">
      <span class="ico" style="left:45px"><svg width="20" height="18" viewBox="0 0 20 18"><path d="M12 1l7 7-7 7v-4c-6 0-9 2-11 6 1-7 4-11 11-12z" fill="#fff"/></svg></span>
      <span class="ico" style="left:120px"><svg width="18" height="18" viewBox="0 0 18 18"><circle cx="7.5" cy="7.5" r="5.5" fill="none" stroke="#fff" stroke-width="2.5"/><path d="M12 12l5 5" stroke="#fff" stroke-width="2.5"/></svg></span>
    </div>
    <div class="g2" role="img" aria-label="Photo of a hand gripping a railing"></div>
    <div class="g3" role="img" aria-label="Photo of bound law reports on a shelf"></div>
    <div class="g4" role="img" aria-label="Photo of a police station lamp"></div>
    <div class="g5" role="img" aria-label="Photo of a law library hall"></div>
  </section>

  <section class="wrap attorneys">
    <h2>Our Attorneys</h2>
    <div class="cards">
      <div class="card">
        <div class="photo dark" role="img" aria-label="Portrait of attorney Owen Hartley"><span></span><span></span><span></span><span></span></div>
        <h4>Owen Hartley</h4><p>Founding Partner · Medicare Fraud</p>
      </div>
      <div class="card">
        <div class="photo" role="img" aria-label="Portrait of attorney Clara Winslow"></div>
        <h4>Clara Winslow</h4><p>Partner · Federal Investigations</p>
      </div>
      <div class="card">
        <div class="photo" role="img" aria-label="Portrait of attorney Martin Ashby"></div>
        <h4>Martin Ashby</h4><p>Senior Counsel · License Defense</p>
      </div>
    </div>
    <div class="dots"><span></span><span class="on"></span><span></span></div>
  </section>

  <section class="wrap stats">
    <div class="stat s1" role="img" aria-label="Background photo of a police lamp on a stone building">
      <div class="cur">$</div><div class="num">48M</div>
      <div class="lab">In alleged losses successfully contested</div>
      <p>Billing disputes can become federal charges. We challenge the numbers before they reach court.</p>
    </div>
    <div class="stat s2" role="img" aria-label="Background photo of a hand on a railing">
      <div class="cur"></div><div class="num">320+</div>
      <div class="lab">Healthcare professionals defended</div>
      <p>Nurses, physicians and clinic owners trust us to protect their freedom, licence and practice.</p>
    </div>
  </section>

  <div class="wrap blog"><span>BLOG PAGE</span></div>
  <div class="wrap partners"><span></span><span></span><span></span><span></span><span></span></div>

  <section class="wrap contact">
    <div class="col">
      <span class="icon"><svg width="16" height="26" viewBox="0 0 16 26"><rect x="1" y="1" width="14" height="24" rx="2" fill="none" stroke="#000" stroke-width="2"/><circle cx="8" cy="21" r="1.5" fill="#000"/></svg></span>
      Phone: 1 (555) 014-2684<br>Fax: 1 (555) 014-2686
    </div>
    <div class="col">
      <span class="icon"><svg width="20" height="26" viewBox="0 0 20 26"><path d="M10 25C4 17 1 13 1 9a9 9 0 0 1 18 0c0 4-3 8-9 16z" fill="#000"/><circle cx="10" cy="9" r="3.5" fill="#fff"/></svg></span>
      PO Box 4410 Elm Row 22,<br>Los Angeles, California,<br>United States
    </div>
    <div class="col">
      <span class="icon"><svg width="26" height="18" viewBox="0 0 26 18"><rect x="1" y="1" width="24" height="16" fill="none" stroke="#000" stroke-width="2"/><path d="M1 1l12 9 12-9" fill="none" stroke="#000" stroke-width="2"/></svg></span>
      help@marvelinlegal.example
    </div>
  </section>

  <section class="wrap write">
    <h2>Write us</h2>
    <div class="sub">Confidential Case Review Form</div>
    <div class="form">
      <div class="field">Full Name</div><div class="field">Phone</div>
      <div class="field">Email Address</div><div class="field">Subject</div>
      <div class="field msg">Message</div>
    </div>
    <span class="send">SEND MESSAGE</span>
  </section>

  <footer class="wrap footer">
    <div class="fcol">
      <h5>RECENT TWEETS</h5>
      <div class="tweet"><i></i><span>New guide on Medicare audit rights is now on our blog</span></div>
      <div class="tweet"><i></i><span>What to do when federal agents visit your clinic</span></div>
      <div class="tweet"><i></i><span>Read our latest notes on billing fraud investigations</span></div>
    </div>
    <div class="fcol">
      <h5>ABOUT US</h5>
      <p>We defend nurses, doctors and clinic owners facing healthcare fraud charges. Early advice protects your licence and your practice. Call us the moment you are contacted by investigators or auditors.</p>
    </div>
    <div class="fcol">
      <h5>CONTACT INFORMATION</h5>
      <div class="row">Reach our defense team any weekday for a confidential review.</div>
      <div class="row">Address: 48 Cedar Court, Los Angeles, CA 90017</div>
      <div class="row">Tel: (555) 014 2291</div>
      <div class="row">Fax: (555) 014 2292</div>
      <div class="row">Email: office@marvelinlegal.example</div>
      <div class="row">Website: www.marvelinlegal.example</div>
    </div>
  </footer>
  <div class="wrap copy">© Marvelin Legal 2015</div>

</div>
</body>
</html>
```